Design Invitation using a mobile phone screen image

This invitation is for 12 year olds finishing primary school so make it fun and bright.
Invitation should be an kavlet with a text message saying.....
Dress in your best (insert emoticons - boy in long pants/girl in dress) for your Year 6 farewell dinner (insert emoticon with tear) on Monday 12 December at 6 pm (insert emoticons - party hat, thumbs up and bowl of icecream). Going 2b a gr8 night!
rsvp YES PLEASE and your name to 0517XXXXXXX

Target Market(s)

12/13 years old boys and girls

Industry/Entity Type

School

Requirements
Must have
• Must be bright and look like a text message - it can have an artwork within it as if the invite has been texted and then a comment is made after the image.
• Must us an kavlet screen as the invitation but so we dont have to cut it out it can be a rectanglar card

```html
<!DOCTYPE html>
<html lang="en">
<head>
<meta charset="utf-8">
<title>Year 6 Farewell Dinner Invitation</title>
<link href="https://fonts.googleapis.com/css2?family=Jost:wght@500;600;700&family=Kaushan+Script&display=swap" rel="stylesheet">
<style>
  :root {
    --page-bg: #dedede;
    --sky-blue: #5d8fd3;
    --sky-deep: #4f80c8;
    --bunting-pink: #f08aa6;
    --bunting-green: #7fd09a;
    --light-yellow: #f4dc6a;
    --cream: #fdfbd6;
    --ink: #1c1c1c;
    --divider: #5a5a5a;
    --ribbon-red: #e3262e;
    --gold: #c38d22;
    --emoji-yellow: #f6c530;
    --emoji-rim: #e2a91c;
    --tile-red: #e3262e;
    --tile-gold: #f2be1e;
    --tile-green: #3aa845;
    --rsvp-red: #ec1c24;
    --white: #ffffff;
  }
  * { box-sizing: border-box; margin: 0; padding: 0; }
  html, body { width: 1200px; height: 1031px; overflow: hidden; }
  body {
    background: var(--page-bg);
    font-family: "Jost", "Futura", sans-serif;
    color: var(--ink);
  }
  .invite {
    position: absolute;
    left: 310px; top: 0;
    width: 579px; height: 1031px;
    background: var(--cream);
    overflow: hidden;
  }

  /* Header artwork area */
  .header-art {
    position: absolute; left: 0; top: 0;
    width: 100%; height: 304px;
    background:
      radial-gradient(ellipse 60% 40% at 20% 30%, rgba(240,138,166,.45), transparent 70%),
      radial-gradient(ellipse 55% 35% at 75% 25%, rgba(127,208,154,.40), transparent 70%),
      radial-gradient(ellipse 70% 30% at 50% 85%, rgba(244,220,106,.35), transparent 70%),
      linear-gradient(180deg, var(--sky-blue) 0%, #6a98d8 55%, var(--sky-deep) 100%);
  }

  .headline {
    position: absolute; top: 324px; left: 0; width: 100%;
    text-align: center;
    font-weight: 600; font-size: 42px; letter-spacing: 1px;
    line-height: 1.2;
  }

  /* Couple emoticon area */
  .couple-art {
    position: absolute; left: 201px; top: 392px;
    width: 174px; height: 185px;
    border-radius: 50% 50% 18px 18px / 34% 34% 18px 18px;
    background: linear-gradient(180deg,
      #f3c33a 0%, #f4cf5a 30%,
      #5a9ae0 44%, #e25a55 72%,
      #f0b43a 100%);
    opacity: .85;
  }

  .ribbon {
    position: absolute; left: 43px; top: 592px;
    width: 491px; height: 35px;
  }
  .ribbon svg { position: absolute; inset: 0; }
  .ribbon-text {
    position: absolute; inset: 0;
    display: flex; align-items: center; justify-content: center; gap: 7px;
    color: var(--white); font-size: 20px; font-weight: 700;
    white-space: nowrap;
  }
  .ribbon-text .script { font-family: "Kaushan Script", cursive; font-weight: 400; font-size: 17px; }

  .occasion {
    position: absolute; left: 86px; top: 645px;
    font-weight: 600; line-height: 1.2;
  }
  .occasion .year { font-size: 33px; display: block; }
  .occasion .dinner { font-size: 33px; display: block; color: var(--gold); }

  /* Sad emoticon area */
  .mood-art {
    position: absolute; left: 416px; top: 659px;
    width: 78px; height: 78px; border-radius: 50%;
    background: radial-gradient(circle at 40% 35%, #fbd95a 0%, var(--emoji-yellow) 55%, #eab226 100%);
    border: 3px solid var(--emoji-rim);
  }

  .divider {
    position: absolute; left: 49px; width: 485px;
    border-top: 3px dotted var(--divider);
  }
  .divider.top { top: 746px; }
  .divider.bottom { top: 790px; }
  .when {
    position: absolute; top: 752px; left: 0; width: 100%;
    text-align: center; font-weight: 600; font-size: 25px; line-height: 34px;
    letter-spacing: .3px;
  }

  /* Icon tiles */
  .icon-tile {
    position: absolute; top: 814px;
    width: 108px; height: 106px;
    border: 4px solid; border-radius: 12px;
    background: var(--white);
    padding: 14px;
  }
  .icon-tile .fill { width: 100%; height: 100%; border-radius: 10px; }
  .tile-party { left: 104px; border-color: var(--tile-red); }
  .tile-party .fill { background: radial-gradient(circle at 50% 40%, #f6d44a 0%, #f08a6a 45%, rgba(234,74,69,.25) 80%, transparent 100%); }
  .tile-approve { left: 236px; border-color: var(--tile-gold); }
  .tile-approve .fill { background: radial-gradient(circle at 50% 50%, #3d7fd4 0%, #5d95dc 45%, rgba(61,127,212,.2) 80%, transparent 100%); }
  .tile-treat { left: 369px; border-color: var(--tile-green); }
  .tile-treat .fill { background: linear-gradient(180deg, rgba(236,47,140,.9) 0%, #f26aa8 40%, #f3c04a 60%, rgba(243,192,74,.3) 100%); }

  .rsvp-band {
    position: absolute; left: 0; top: 944px;
    width: 100%; height: 87px;
    background: var(--sky-blue);
    text-align: center;
  }
  .rsvp-title {
    color: var(--rsvp-red); font-weight: 700; font-size: 30px;
    line-height: 1; padding-top: 14px;
  }
  .rsvp-detail {
    font-weight: 600; font-size: 18px; line-height: 1; margin-top: 13px;
  }
</style>
</head>
<body>
  <main class="invite">
    <div class="header-art" role="img" aria-label="Hand-drawn bunting, fairy lights and stars on blue with the lettering Farewell to Summer"></div>

    <h1 class="headline">DRESS IN YOUR BEST</h1>
    <div class="couple-art" role="img" aria-label="Emoticon of a boy in long pants and a girl in a dress holding hands"></div>

    <div class="ribbon">
      <svg viewBox="0 0 491 35" width="491" height="35" aria-hidden="true">
        <polygon points="0,0 491,0 479,17.5 491,35 0,35 12,17.5" fill="var(--ribbon-red)"/>
      </svg>
      <p class="ribbon-text">
        <span class="script">Hope u Can</span><span>MAKE IT.</span>
        <span class="script">Going to</span><span>BE GREAT</span>
      </p>
    </div>

    <p class="occasion">
      <span class="year">FOR YOUR YEAR 6</span>
      <span class="dinner">FAREWELL DINNER</span>
    </p>
    <div class="mood-art" role="img" aria-label="Sad emoticon with a tear"></div>

    <div class="divider top"></div>
    <p class="when">ON MONDAY 12 DECEMBER AT 6 PM</p>
    <div class="divider bottom"></div>

    <div class="icon-tile tile-party"><div class="fill" role="img" aria-label="Party hat emoticon"></div></div>
    <div class="icon-tile tile-approve"><div class="fill" role="img" aria-label="Thumbs up emoticon"></div></div>
    <div class="icon-tile tile-treat"><div class="fill" role="img" aria-label="Ice cream emoticon"></div></div>

    <footer class="rsvp-band">
      <p class="rsvp-title">RSVP</p>
      <p class="rsvp-detail">Yes Please And Your Name To 0517XXXXXXX</p>
    </footer>
  </main>
</body>
</html>
```